Kestrel Aid Services Banner Ad

Need a 750 x 250-pixel banner ad with the company Logo included. Please see company website at www.kestrelaidservices.com for more information.

```html
<!DOCTYPE html>
<html lang="en">
<head>
<meta charset="utf-8">
<title>Kestrel Aid Services Banner Ad</title>
<link href="https://fonts.googleapis.com/css2?family=Roboto+Condensed:wght@700&family=Roboto:ital,wght@0,300;0,400;1,400&display=swap" rel="stylesheet">
<style>
  :root {
    --page: #f5f2ed;
    --panel: #f5f5f7;
    --band-grey: #ececec;
    --slash-grey: #e0e0e0;
    --green: #6ab522;
    --green-dark: #3d8a3a;
    --teal: #1a5c78;
    --navy: #0c2b52;
    --navy-deep: #071f40;
    --white: #ffffff;
    --ink: #1c2f4f;
  }
  * { margin: 0; padding: 0; box-sizing: border-box; }
  html, body { width: 1200px; height: 900px; overflow: hidden; }
  body { background: var(--page); position: relative; font-family: "Roboto", Arial, sans-serif; }

  .banner {
    position: absolute; left: 137px; top: 285px;
    width: 930px; height: 310px;
    background: var(--panel);
    overflow: hidden;
    box-shadow: 0 1px 3px rgba(0,0,0,0.06);
  }
  .banner__shapes, .banner__photo { position: absolute; inset: 0; width: 930px; height: 310px; }

  .headline {
    position: absolute; left: 30px; top: 26px;
    font-family: "Roboto Condensed", "Arial Narrow", sans-serif;
    font-weight: 700; font-size: 44px; line-height: 1;
    color: var(--green); letter-spacing: -0.5px;
  }
  .subhead {
    position: absolute; left: 30px; top: 82px;
    font-family: "Roboto", Arial, sans-serif;
    font-weight: 300; font-size: 29px; line-height: 1;
    color: var(--ink); letter-spacing: -0.5px;
  }
  .tagline {
    position: absolute; left: 30px; top: 128px;
    padding-left: 10px;
    border-left: 2px solid var(--green);
    font-style: italic; font-size: 13.5px; line-height: 18px;
    color: var(--ink); letter-spacing: -0.3px;
  }

  .contact { position: absolute; left: 30px; top: 248px; color: var(--white); }
  .contact__call { display: flex; align-items: center; gap: 8px; }
  .contact__icon { width: 25px; height: 25px; }
  .contact__phone {
    font-family: "Roboto Condensed", "Arial Narrow", sans-serif;
    font-weight: 700; font-size: 20px; letter-spacing: -0.2px;
  }
  .contact__web { margin-top: 5px; font-size: 14px; }

  .brand {
    position: absolute; right: 20px; bottom: 20px;
    display: flex; align-items: center; gap: 7px;
    font-family: "Roboto Condensed", "Arial Narrow", sans-serif;
    font-weight: 700; font-size: 21px; color: var(--green);
  }
  .brand__dot { width: 12px; height: 12px; border-radius: 50%; background: var(--navy); }
</style>
</head>
<body>
  <section class="banner">
    <svg class="banner__shapes" viewBox="0 0 930 310" aria-hidden="true">
      <defs>
        <linearGradient id="navyFill" x1="0" y1="0" x2="0" y2="1">
          <stop offset="0" stop-color="var(--navy)"/>
          <stop offset="1" stop-color="var(--navy-deep)"/>
        </linearGradient>
        <linearGradient id="tealFill" x1="0" y1="1" x2="1" y2="0">
          <stop offset="0" stop-color="var(--teal)"/>
          <stop offset="1" stop-color="#0f4f80"/>
        </linearGradient>
      </defs>
      <!-- title band and grey slash -->
      <rect class="title-band" x="0" y="20" width="470" height="61" fill="var(--band-grey)"/>
      <polygon class="grey-slash" points="416,20 519,20 650,92 590,124" fill="var(--slash-grey)"/>
      <!-- white right area -->
      <polygon class="white-field" points="853,0 930,0 930,310 300,310" fill="var(--white)"/>
      <!-- navy corner and band -->
      <polygon class="navy-field" points="0,170 300,240 808,0 853,0 432,240 297,310 0,310" fill="url(#navyFill)"/>
      <!-- teal band -->
      <polygon class="teal-band" points="440,243 800,12 808,0 790,0 452,226 470,232" fill="url(#tealFill)"/>
      <!-- green stripes -->
      <polygon class="green-stripe" points="744,0 796,0 480,208 452,226 410,222" fill="var(--green)"/>
      <polygon class="green-stripe-dark" points="796,0 808,0 475,250 460,250" fill="var(--green-dark)"/>
    </svg>

    <svg class="banner__photo" viewBox="0 0 930 310" role="img" aria-label="Photo of a smiling young man in a wheelchair raising both arms in celebration on a city street">
      <defs>
        <linearGradient id="photoFill" x1="0" y1="0" x2="1" y2="1">
          <stop offset="0" stop-color="#8a7a6e"/>
          <stop offset="0.5" stop-color="#4d5a78"/>
          <stop offset="1" stop-color="#c4bcb4"/>
        </linearGradient>
      </defs>
      <polygon points="904,0 930,0 930,141 619,310 354,310" fill="url(#photoFill)"/>
    </svg>

    <h1 class="headline">Support Coordination</h1>
    <p class="subhead">Across New Jersey</p>
    <p class="tagline">We promote a “can do” attitude knowing that<br>everything is possible once you believe in yourself.</p>

    <div class="contact">
      <div class="contact__call">
        <svg class="contact__icon" viewBox="0 0 24 24" aria-hidden="true">
          <circle cx="12" cy="12" r="12" fill="var(--green)"/>
          <path d="M9.2 6.5c.4-.2.9-.1 1.1.3l1 2c.2.4.1.8-.2 1.1l-.8.7c.5 1.2 1.6 2.4 2.9 3l.7-.8c.3-.3.8-.4 1.1-.2l2 1c.4.2.5.7.3 1.1l-.6 1.1c-.3.5-.9.8-1.5.7-3.5-.7-6.3-3.5-7-7-.1-.6.2-1.2.7-1.5z" fill="var(--navy)"/>
        </svg>
        <span class="contact__phone">CALL US! 609-555-0148</span>
      </div>
      <p class="contact__web">www.kestrelaidservices.com</p>
    </div>

    <div class="brand">
      <span class="brand__dot"></span>
      <span class="brand__name">Kestrel Aid Services</span>
    </div>
  </section>
</body>
</html>
```